Innovative Event Ticketing Start Up. Needs a Web Design

We need a web design for a new company based in London called 'Brimwell'. We are a platform which facilitates the building of groups of customers for events. As more people commit to an event, the price incrementally decreases. We would like there to be an emphasis on the sharing element and the decreasing price with higher participation.

Any quieres please email me at jrvk58@postvale.com

Target Market(s)

18-30 year olds who are active and savvy across social media sites

Industry/Entity Type

Events

Number of Pages Required

3 page

Font styles to use
Other font styles liked:
• Phi Roman

Requirements
Must have
• Each event offering runs for a limited time so a countdown timer is also to be included as well as a counter of number of participants (please find example attached).
• The interface needs to have the options for 'Live 'Music', 'Nightlife', 'Festivals', 'Comedy' and 'Everything Else'. Also
• A 'featured' section, for our promoted events
• Social sharing icons for Friendloom, Zephly, Pingrove, SMS and Email
• Room the inclusion of a video
• Pages for clients to sign up - registering details ect.
• Content is still being completed, so room available to add when ready
Nice to have
• An interface design we like as a guiding templates on is https://quorvexapp.com/
• Velto wordpress theme is also of interest.
• Scroll over clicking for main interface and also for the event once clicked upon.
• Event pages similar desgin to quorvex with same features such as Orvane Atlas but also participant counter and affiliate marketing options.
Should not have
• CMS no longer necessary

```html
<!DOCTYPE html>
<html lang="en">
<head>
<meta charset="utf-8">
<title>Brimwell</title>
<link href="https://fonts.googleapis.com/css2?family=Lato:wght@400;700;900&display=swap" rel="stylesheet">
<style>
:root{
  --orange:#f0522a;
  --black:#111111;
  --ink:#222222;
  --muted:#666666;
  --band:#efefef;
  --white:#ffffff;
  --line:#dddddd;
}
*{box-sizing:border-box;margin:0;padding:0}
html,body{width:1200px;height:2492px;overflow:hidden;background:var(--white);font-family:"Lato",Arial,sans-serif;color:var(--ink)}
.page{position:relative;width:1200px;height:2492px;overflow:hidden}
.topbar{height:60px;display:flex;align-items:center;justify-content:space-between;padding:0 24px}
.brand{display:flex;align-items:center;gap:10px;font-weight:900;font-size:26px;color:var(--orange);letter-spacing:1px;text-transform:uppercase}
.brand-mark{width:30px;height:30px;background:var(--orange)}
.btn{display:inline-block;background:var(--black);color:var(--white);font-weight:700;border-radius:4px}
.signup{padding:9px 22px;font-size:15px}
.nav{height:52px;background:var(--orange);display:flex;align-items:center;gap:62px;padding-left:92px}
.nav a{color:var(--white);text-decoration:none;font-size:16px}
.hero{position:relative;height:448px;background:linear-gradient(180deg,#f4e7d8 0%,#e9b27a 30%,#b4502a 62%,#2a1410 100%);text-align:center}
.hero-copy{padding-top:36px}
.hero h1{font-size:32px;font-weight:900;color:var(--black);max-width:960px;margin:0 auto}
.hero p{font-size:13px;color:#333;max-width:760px;margin:12px auto 0;line-height:1.45}
.register{margin-top:18px;padding:12px 24px;font-size:16px}
.video-section{display:flex;gap:36px;padding:100px 88px 0;height:420px}
.video{position:relative;width:572px;height:320px;background:#1d1d1d;padding:26px}
.video-screen{width:100%;height:250px;background:linear-gradient(135deg,#f26a3c,#e14a20);display:flex;align-items:center;justify-content:center}
.video-bar{position:absolute;left:26px;right:26px;bottom:20px;height:8px;background:#444}
.video-bar span{display:block;width:40%;height:100%;background:var(--orange)}
.video-text{width:420px;padding-top:24px}
.video-text h3{font-size:17px;font-weight:900;line-height:1.35}
.video-text p{font-size:13px;line-height:1.7;color:var(--muted);margin-top:18px}
.categories{display:flex;gap:24px;padding:32px 88px 0;height:272px}
.cat{width:234px;height:240px;background:var(--black);border-radius:6px;color:var(--white);text-align:center;padding:26px 24px}
.cat svg{display:block;margin:0 auto}
.cat h4{font-size:25px;font-weight:700;margin-top:10px}
.cat p{font-size:12px;line-height:1.6;color:#cfcfcf;margin-top:8px}
.intro{display:flex;gap:40px;padding:16px 88px 0;height:230px}
.intro h2{width:480px;text-align:right;font-size:31px;font-weight:900;line-height:1.3;color:var(--black)}
.intro-body{width:492px}
.intro-body h5{font-size:15px;font-weight:900}
.intro-body p{font-size:12.5px;line-height:1.7;color:var(--muted);margin-top:6px}
.read-more{display:inline-block;background:var(--orange);color:var(--white);font-size:13px;padding:8px 14px;margin-top:10px}
.featured{background:var(--band);height:760px;padding:50px 88px 0}
.featured h2{text-align:center;font-size:24px;font-weight:900;color:var(--black);line-height:30px}
.featured-lead{text-align:center;font-size:13px;color:var(--muted);line-height:1.7;max-width:900px;margin:24px auto 30px;height:44px}
.event{display:flex;height:170px;margin-bottom:22px;background:var(--white);overflow:hidden}
.event-days{flex:0 0 200px;background:var(--orange);color:var(--black);font-size:28px;font-weight:700;display:flex;align-items:center;justify-content:center}
.event-body{display:flex;gap:28px;padding:22px 30px}
.event-photo{flex:0 0 80px;height:110px;background:linear-gradient(160deg,#d7c2e4,#7a4c8a)}
.event-info h4{font-size:16px;font-weight:700;color:var(--orange);line-height:20px}
.event-info p{font-size:13px;line-height:21px;color:var(--muted);margin-top:6px;max-width:660px}
.participants{padding:9px 14px;font-size:13px;margin-top:12px}
.social{display:flex;align-items:center;justify-content:center;gap:18px;height:100px}
.social strong{font-size:22px;font-weight:900;margin-right:10px}
.social .dot{width:40px;height:40px;border-radius:50%;background:var(--black)}
.contacts{display:flex;justify-content:center;gap:110px;height:70px;align-items:center}
.contact{display:flex;align-items:center;gap:16px;font-size:16px}
.contact .ic{width:50px;height:50px;border-radius:50%;background:var(--orange);display:flex;align-items:center;justify-content:center}
.footer{position:absolute;left:0;right:0;bottom:0;height:60px;border-top:1px solid var(--line);text-align:center;line-height:60px;font-size:14px;color:var(--muted)}
</style>
</head>
<body>
<div class="page">
  <header class="topbar">
    <div class="brand"><span class="brand-mark"></span>Brimwell</div>
    <span class="btn signup">Sign Up</span>
  </header>
  <nav class="nav">
    <a href="#">Home</a><a href="#">About</a><a href="#">Events</a><a href="#">Schedule</a><a href="#">Participants</a><a href="#">Contact Us</a>
  </nav>

  <section class="hero" role="img" aria-label="Concert crowd with raised hands under warm stage lights">
    <div class="hero-copy">
      <h1>Contrary to popular belief, Lorem Ipsum is not simply random text</h1>
      <p>There are many variations of passages of Lorem Ipsum available, but the majority have suffered alteration in some form, by injected humour, or randomised words which don't look even slightly believable at all.</p>
      <span class="btn register">Register Now</span>
    </div>
  </section>

  <section class="video-section">
    <div class="video">
      <div class="video-screen" role="img" aria-label="Event promo video">
        <svg width="90" height="90" viewBox="0 0 90 90"><circle cx="45" cy="45" r="40" fill="#ffffff" opacity=".9"/><rect x="34" y="28" width="8" height="34" fill="#f0522a"/><rect x="48" y="28" width="8" height="34" fill="#f0522a"/></svg>
      </div>
      <div class="video-bar"><span></span></div>
    </div>
    <div class="video-text">
      <h3>Lorem Ipsum is simply dummy text of the printing and typesetting</h3>
      <p>Lorem ipsum dolor sit amet, consectetur adipiscing elit, sed do eiusmod tempor incididunt ut labore et dolore magna aliqua. Ut enim ad minim veniam, quis nostrud exercitation ullamco laboris nisi ut aliquip ex ea commodo consequat. Duis aute irure dolor in reprehenderit in voluptate velit esse cillum dolore eu fugiat nulla pariatur, excepteur sint occaecat cupidatat non proident.</p>
    </div>
  </section>

  <section class="categories">
    <div class="cat">
      <svg width="60" height="60" viewBox="0 0 60 60"><path d="M22 44V14l26-6v30" fill="none" stroke="#f0522a" stroke-width="4"/><circle cx="17" cy="44" r="7" fill="#f0522a"/><circle cx="43" cy="38" r="7" fill="#f0522a"/></svg>
      <h4>Live Music</h4>
      <p>Lorem ipsum dolor sit amet, consectetur adipiscing elit sed do eiusmod.</p>
    </div>
    <div class="cat">
      <svg width="60" height="60" viewBox="0 0 60 60"><path d="M14 10h32L30 32z" fill="#f0522a"/><path d="M30 32v18M20 52h20" stroke="#f0522a" stroke-width="4"/></svg>
      <h4>Nightlife</h4>
      <p>Lorem ipsum dolor sit amet, consectetur adipiscing elit sed do eiusmod.</p>
    </div>
    <div class="cat">
      <svg width="60" height="60" viewBox="0 0 60 60"><g stroke="#f0522a" stroke-width="4" stroke-linecap="round"><path d="M30 8v44M12 16l36 28M48 16L12 44"/></g><circle cx="30" cy="30" r="6" fill="#f0522a"/></svg>
      <h4>Festivals</h4>
      <p>Lorem ipsum dolor sit amet, consectetur adipiscing elit sed do eiusmod.</p>
    </div>
    <div class="cat">
      <svg width="60" height="60" viewBox="0 0 60 60"><rect x="24" y="8" width="12" height="24" rx="6" fill="#f0522a"/><path d="M16 28a14 14 0 0 0 28 0M30 42v12" fill="none" stroke="#f0522a" stroke-width="4"/></svg>
      <h4>Comedy</h4>
      <p>Lorem ipsum dolor sit amet, consectetur adipiscing elit sed do eiusmod.</p>
    </div>
  </section>

  <section class="intro">
    <h2>LOREM IPSUM IS SIMPLY DUMMY TEXT OF THE PRINTING HE STANDARD CHUNK OF</h2>
    <div class="intro-body">
      <h5>LOREM IPSUM IS SIMPLY DUMMY TEXT OF THE PRINTING AND</h5>
      <p>Contrary to popular belief, Lorem Ipsum is not simply random text. Sed ut perspiciatis unde omnis iste natus error sit voluptatem accusantium doloremque laudantium, totam rem aperiam, eaque ipsa quae ab illo inventore veritatis et quasi architecto beatae vitae dicta sunt explicabo. Nemo enim ipsam voluptatem quia voluptas sit aspernatur aut odit aut fugit, sed quia consequuntur magni dolores.</p>
      <span class="read-more">Read more</span>
    </div>
  </section>

  <section class="featured">
    <h2>FEATURED PROMOTED EVENTS</h2>
    <p class="featured-lead">Lorem ipsum dolor sit amet, consectetur adipiscing elit, sed do eiusmod tempor incididunt ut labore et dolore magna aliqua. Ut enim ad minim veniam, quis nostrud exercitation ullamco laboris nisi ut aliquip ex ea commodo consequat duis aute irure dolor.</p>
    <div class="event">
      <div class="event-days">10 DAYS</div>
      <div class="event-body">
        <div class="event-photo" role="img" aria-label="Event poster"></div>
        <div class="event-info">
          <h4>Lorem Ipsum is simply dummy text of the printing and typesetting</h4>
          <p>Lorem ipsum dolor sit amet, consectetur adipiscing elit, sed do eiusmod tempor incididunt ut labore et dolore magna aliqua. Ut enim ad minim veniam, quis nostrud exercitation ullamco.</p>
          <span class="btn participants">100 Participants</span>
        </div>
      </div>
    </div>
    <div class="event">
      <div class="event-days">20 DAYS</div>
      <div class="event-body">
        <div class="event-photo" role="img" aria-label="Event poster" style="background:linear-gradient(160deg,#f6c07a,#c4541f)"></div>
        <div class="event-info">
          <h4>Lorem Ipsum is simply dummy text of the printing and typesetting</h4>
          <p>Lorem ipsum dolor sit amet, consectetur adipiscing elit, sed do eiusmod tempor incididunt ut labore et dolore magna aliqua. Ut enim ad minim veniam, quis nostrud exercitation ullamco.</p>
          <span class="btn participants">100 Participants</span>
        </div>
      </div>
    </div>
    <div class="event">
      <div class="event-days">30 DAYS</div>
      <div class="event-body">
        <div class="event-photo" role="img" aria-label="Event poster" style="background:linear-gradient(160deg,#f2d9c6,#8a5a86)"></div>
        <div class="event-info">
          <h4>Lorem Ipsum is simply dummy text of the printing and typesetting</h4>
          <p>Lorem ipsum dolor sit amet, consectetur adipiscing elit, sed do eiusmod tempor incididunt ut labore et dolore magna aliqua. Ut enim ad minim veniam, quis nostrud exercitation ullamco.</p>
          <span class="btn participants">100 Participants</span>
        </div>
      </div>
    </div>
  </section>

  <section class="social">
    <strong>We are Social</strong>
    <span class="dot" aria-label="Friendloom"></span>
    <span class="dot" aria-label="Zephly"></span>
    <span class="dot" aria-label="Pingrove"></span>
    <span class="dot" aria-label="SMS"></span>
    <span class="dot" aria-label="Email"></span>
  </section>

  <section class="contacts">
    <div class="contact"><span class="ic"><svg width="22" height="26" viewBox="0 0 22 26"><path d="M11 1a9 9 0 0 0-9 9c0 7 9 15 9 15s9-8 9-15a9 9 0 0 0-9-9z" fill="#fff"/><circle cx="11" cy="10" r="3.5" fill="#f0522a"/></svg></span>4820 Harlow Lane 5507213</div>
    <div class="contact"><span class="ic"><svg width="24" height="24" viewBox="0 0 24 24"><path d="M6 2l4 5-2 3c1 3 3 5 6 6l3-2 5 4-2 4C10 22 2 14 2 4z" fill="#fff"/></svg></span>412 608 935</div>
    <div class="contact"><span class="ic"><svg width="24" height="18" viewBox="0 0 24 18"><rect x="1" y="1" width="22" height="16" fill="#fff"/><path d="M1 1l11 9 11-9" fill="none" stroke="#f0522a" stroke-width="2"/></svg></span>info@brimwell.com</div>
  </section>

  <footer class="footer">©2022 Brimwell. All Rights Reserved</footer>
</div>
</body>
</html>
```